Simple, Professional and neat business card design for Vendralo Inc.

We're looking to re-vamp our business card design. We're a supplier of innovative feed ingredients for the North American animal agriculture industry. We are located in Lucknow, Ontario, Canada and our flagship product is a product that prevents milk fever in dairy cows when the calve, it is fed before calving and is very effective compared to other alternatives available on the market today.

Our company has Danish roots and we import all of our product from our Danish partner/manufacturer in Denmark. We like our design to embrace high professionalism while remaining neat and simple.

Target Market(s)

B2B, Feed Mills, Veterinary Clinics, Large integrators/producers,

Industry/Entity Type

Agribusiness

Contact Information for Business Card

We like the rounded corners because they make the card easy to sit in a wallet and not many use it so it makes the card stand out, just possibly something to take account for during the design.

As you can also see on the sliders below, looking for a that simple but proffesional scandinavian design.

Requirements
Nice to have
• Rounded corners
Should not have
• Too vibrant

```html
<!DOCTYPE html>
<html lang="en">
<head>
<meta charset="utf-8">
<title>Vendralo Inc. — Business Card</title>
<link href="https://fonts.googleapis.com/css2?family=Lato:wght@700;900&family=Montserrat:wght@400;600;700&display=swap" rel="stylesheet">
<style>
  :root{
    --bg:#2b2b2b;
    --card:#1e1e1e;
    --brand-blue:#1360b4;
    --brand-gold:#c9b488;
    --text-light:#d9d9d9;
    --icon-line:#a8a8a8;
  }
  html,body{margin:0;padding:0;overflow:hidden;}
  body{width:1200px;height:900px;background:var(--bg);position:relative;font-family:"Montserrat",sans-serif;}
  .card{position:absolute;top:252px;width:504px;height:280px;border-radius:24px;background:var(--card);box-shadow:0 6px 14px rgba(0,0,0,.45);overflow:hidden;}
  .card--front{left:78px;}
  .card--back{left:616px;}
  .brand-mark{position:absolute;border-radius:50%;background:var(--brand-gold);}
  .brand-name{position:absolute;margin:0;font-family:"Lato",sans-serif;font-weight:900;color:var(--brand-blue);letter-spacing:-0.5px;white-space:nowrap;line-height:1;}
  .card--front .brand-mark{left:30px;top:46px;width:74px;height:74px;}
  .card--front .brand-name{left:115px;top:68px;font-size:30px;}
  .person-name{position:absolute;left:29px;top:158px;margin:0;font-weight:600;font-size:15px;letter-spacing:1px;color:var(--brand-blue);padding-bottom:3px;border-bottom:1.5px solid var(--text-light);}
  .contact-row{position:absolute;left:28px;display:flex;gap:14px;font-size:10.5px;color:var(--text-light);}
  .contact-row--first{top:187px;}
  .contact-row--second{top:211px;}
  .contact-item{display:flex;align-items:center;gap:6px;}
  .contact-icon{width:13px;height:13px;flex:none;}
  .company-line{position:absolute;left:28px;top:232px;margin:0;font-weight:700;font-size:10.5px;color:var(--brand-blue);}
  .address-line{position:absolute;left:28px;top:246px;margin:0;font-size:10.5px;color:var(--text-light);}
  .card--back .brand-mark{left:53px;top:98px;width:93px;height:93px;}
  .card--back .brand-name{left:164px;top:116px;font-size:38px;}
  .tagline{position:absolute;left:165px;top:160px;margin:0;font-size:8.5px;color:var(--brand-blue);white-space:nowrap;}
  .tagline span{margin:0 12px;}
  .showcase-lockup .brand-mark{left:300px;top:620px;width:108px;height:108px;}
  .showcase-lockup .brand-name{left:440px;top:643px;font-size:58px;}
</style>
</head>
<body>
  <section class="card card--front">
    <div class="brand-mark"></div>
    <h1 class="brand-name">VENDRALO INC.</h1>
    <h2 class="person-name">MIKKEL SORENSEN</h2>
    <div class="contact-row contact-row--first">
      <span class="contact-item"><svg class="contact-icon" viewBox="0 0 14 14"><circle cx="7" cy="7" r="6.2" fill="none" stroke="var(--icon-line)"/><rect x="5" y="3.5" width="4" height="7" rx="0.8" fill="none" stroke="var(--icon-line)"/></svg>519-410-2276</span>
      <span class="contact-item"><svg class="contact-icon" viewBox="0 0 14 14"><circle cx="7" cy="7" r="6.2" fill="none" stroke="var(--icon-line)"/><path d="M4 8.5h6l-1-3H5z" fill="var(--icon-line)"/></svg>519-604-3318</span>
      <span class="contact-item"><svg class="contact-icon" viewBox="0 0 14 14"><circle cx="7" cy="7" r="6.2" fill="none" stroke="var(--icon-line)"/><path d="M4.5 4c0 3 2.5 5.5 5.5 5.5l.5-1.3-1.5-.8-.7.7C7.3 7.6 6.4 6.7 5.9 5.7l.7-.7-.8-1.5z" fill="var(--icon-line)"/></svg>888-507-4462 [toll free]</span>
    </div>
    <div class="contact-row contact-row--second">
      <span class="contact-item"><svg class="contact-icon" viewBox="0 0 14 14"><circle cx="7" cy="7" r="6.2" fill="var(--icon-line)"/><rect x="4" y="5" width="6" height="4" fill="var(--card)"/></svg>519-604-3390</span>
      <span class="contact-item"><svg class="contact-icon" viewBox="0 0 14 14"><circle cx="7" cy="7" r="6.2" fill="none" stroke="var(--icon-line)"/><rect x="4" y="4.8" width="6" height="4.4" fill="var(--icon-line)"/></svg>mikkel@vendralo.com</span>
      <span class="contact-item"><svg class="contact-icon" viewBox="0 0 14 14"><circle cx="7" cy="7" r="6.2" fill="none" stroke="var(--icon-line)"/><circle cx="7" cy="7" r="3" fill="none" stroke="var(--icon-line)"/><path d="M4 7h6" stroke="var(--icon-line)"/></svg>www.vendralo.com</span>
    </div>
    <p class="company-line">VENDRALO INCORPORATION</p>
    <p class="address-line">Box 240, Harrowdale, Ontario Canada N0X 1K0</p>
  </section>

  <section class="card card--back">
    <div class="brand-mark"></div>
    <h1 class="brand-name">VENDRALO INC.</h1>
    <p class="tagline">Preventative Care<span>|</span>High-Performance<span>|</span>Prescription-Free</p>
  </section>

  <section class="showcase-lockup">
    <div class="brand-mark"></div>
    <h1 class="brand-name">VENDRALO INC.</h1>
  </section>
</body>
</html>
```